magcian / mentalist needs flyer desined to send potentisl clients

I need a design that's contemporary, sharp, fun, and professional that will get the attention of whoever receives the flyer very quickly. This is for a tri-fold flyer design.

I've been performing magic for over 40 years. I've performed close-up,
parlor, and stage shows. I've been an Master of Ceremonies, Key Note
Speaker (using magic during presentations to help build on a point or
topic, while keeping the audience entertained and educated on the topic or
topics the client has asked me to focus). I've worked trade shows and
sales training incorporating magic as well. I did private shows in Las
Vegas and L.A. back in the late 90's as well.

I do have website / wesleytorvandmagic.example for your to check out.

Target Market(s)

The target audience is corporation Event Planners, Marketing and Sales
managers, casino & hotel entertainment directors, as well as private
businesses looking for unique entertainment options.

Industry/Entity Type

Entertainment Industry

Logo Text

Here are a couple of ideas: your mind is my playground, neural entertainer, professor of mysteries, master of your mind

Requirements
Must have
• I like the black and white look (I think it looks nice, but open to other
• ideas and creativity. Being I'm a magician and mentalist, I'd like for
• both venues to be conveyed somehow. My magic is clean and corporate and family friendly.
Nice to have
• I do have website / wesleytorvandmagic.example for your to check out.
• My current business card is attached for review. I'll also attach photos
• I'd like to share, but was unable when I last attempted do sign up. Some
• of the files were too big and I'm not savvy enough to make them smaller,
• but think there might be some potential with a couple.
Should not have
• cartoons or cartoonish graphics. no rabbits, doves, magicians, wands, or top hats.

```html
<!DOCTYPE html>
<html lang="en">
<head>
<meta charset="utf-8">
<title>Wesley Torvand – Corporate Magician Tri-fold</title>
<link rel="stylesheet" href="https://fonts.googleapis.com/css2?family=Cinzel:wght@400;700&family=Lato:ital,wght@0,400;0,700;1,700&family=Oswald:wght@500;700&display=swap">
<style>
:root{
  --backdrop:#9d8b71;
  --red:#d9131c;
  --red-bright:#f0262d;
  --red-dark:#5e080b;
  --black:#0c0c0c;
  --charcoal:#1e1e1e;
  --silver:#d4d7db;
  --white:#ffffff;
  --photo-warm:#6b4d3e;
  --photo-dark:#1a1618;
}
*{box-sizing:border-box;margin:0;padding:0}
html,body{width:907px;height:1200px;overflow:hidden}
body{background:var(--backdrop);font-family:'Lato',sans-serif;color:var(--white);position:relative}
.sheet{position:absolute;left:62px;width:793px;height:565px;overflow:hidden;background:var(--black);box-shadow:0 3px 10px rgba(0,0,0,.45)}
.sheet--outside{top:27px}
.sheet--inside{top:617px}
.sheet-art{position:absolute;inset:0}
.photo{position:absolute}
.abs{position:absolute}
.serif-heading{font-family:'Cinzel',serif;text-transform:uppercase}
.body-copy{font-size:9.2px;line-height:1.22;text-align:justify}
.body-copy p{margin-bottom:1px}
.brand-name{font-family:'Cinzel',serif;font-weight:700;color:var(--white);letter-spacing:.5px;text-transform:uppercase;white-space:nowrap}
.dropcap{font-family:'Cinzel',serif;font-size:15px;line-height:1}

/* outside */
.about-heading{left:0;width:250px;top:241px;text-align:right;font-size:14px;font-weight:700}
.about-copy{left:10px;top:260px;width:248px}
.studio-block{left:266px;width:262px;text-align:center}
.studio-name{top:348px;font-weight:700;font-size:15px}
.studio-phone{top:364px;font-family:'Oswald',sans-serif;font-weight:500;font-size:31px;letter-spacing:.5px}
.contact-list{left:293px;top:410px;list-style:none;font-weight:700;font-size:12px}
.contact-list li{display:flex;align-items:center;gap:8px;height:23.5px}
.contact-list svg{flex:none}
.cover-title{left:528px;width:265px;text-align:center}
.cover-band{left:540px;top:84px;width:240px;height:30px;background:var(--red);font-family:'Oswald',sans-serif;font-weight:700;font-size:21px;line-height:30px;text-align:center;letter-spacing:.4px}
.cover-years{top:120px;font-family:'Cinzel',serif;font-size:21px}
.roles-pill{left:553px;top:486px;width:216px;height:20px;border:2px solid var(--silver);border-radius:4px;background:var(--black);display:flex;justify-content:space-around;align-items:center;font-size:10.5px;font-weight:700;transform:skewX(-14deg)}
.roles-pill span{transform:skewX(14deg)}
.dot::before{content:"";display:inline-block;width:5px;height:5px;border-radius:50%;background:var(--red-bright);margin-right:3px;vertical-align:1px}
.cover-url{left:528px;width:265px;top:549px;text-align:center;font-weight:700;font-size:10.5px;letter-spacing:2.6px}

/* inside */
.badge{height:28px;border:2px solid var(--silver);display:flex;align-items:center;justify-content:center;font-family:'Oswald',sans-serif;font-weight:700;font-size:20px;letter-spacing:.5px;clip-path:polygon(9% 0,91% 0,100% 50%,91% 100%,9% 100%,0 50%)}
.badge--dark{left:55px;top:277px;width:152px;background:var(--black)}
.badge--red{left:323px;top:276px;width:152px;background:var(--red)}
.bullets{list-style:none;display:grid;grid-template-columns:1fr 1fr;column-gap:10px;row-gap:2px;font-size:10px;font-weight:700;font-style:italic}
.bullets li{display:flex;gap:5px;align-items:flex-start;line-height:1.2}
.bullets li::before{content:"";flex:none;width:5px;height:5px;border-radius:50%;background:var(--white);margin-top:4px}
.bullets--red li::before{background:var(--red-bright)}
.what-list{left:20px;top:318px;width:230px}
.what-copy{left:20px;top:376px;width:232px;font-size:9.2px;line-height:1.25}
.services-intro{left:282px;top:320px;width:230px;font-size:9.2px;line-height:1.25}
.services-list{left:282px;top:374px;width:230px;row-gap:6px}
.promise{left:538px;width:245px;text-align:center}
.promise-kicker{font-family:'Cinzel',serif;font-size:12px;font-weight:700}
.promise-big{font-family:'Cinzel',serif;font-size:20px;line-height:1.05}
.promise-huge{font-family:'Cinzel',serif;font-size:26px;line-height:1}
.promise-copy{left:546px;width:236px;font-size:8.6px;line-height:1.24;text-align:left}
</style>
</head>
<body>

<!-- OUTSIDE -->
<section class="sheet sheet--outside">
  <svg class="sheet-art" width="793" height="565" viewBox="0 0 793 565" aria-hidden="true">
    <defs>
      <linearGradient id="redPanel" x1="0" y1="0" x2="0.4" y2="1">
        <stop offset="0" stop-color="#a80c12"/>
        <stop offset=".45" stop-color="#e0151d"/>
        <stop offset="1" stop-color="#7a090d"/>
      </linearGradient>
      <linearGradient id="midPanel" x1="0" y1="0" x2="0" y2="1">
        <stop offset="0" stop-color="#161616"/>
        <stop offset=".5" stop-color="#262626"/>
        <stop offset="1" stop-color="#141414"/>
      </linearGradient>
      <radialGradient id="coverGlow" cx=".5" cy=".22" r=".6">
        <stop offset="0" stop-color="#3a3a3a"/>
        <stop offset="1" stop-color="#0a0a0a"/>
      </radialGradient>
    </defs>
    <rect x="0" y="0" width="266" height="565" fill="var(--black)"/>
    <polygon points="0,212 266,176 266,565 0,565" fill="url(#redPanel)"/>
    <polygon points="0,52 120,22 266,22 266,12 118,12 0,42" fill="var(--red)"/>
    <polygon points="0,220 266,184 266,192 0,228" fill="var(--silver)"/>
    <rect x="266" y="0" width="262" height="565" fill="url(#midPanel)"/>
    <rect x="528" y="0" width="265" height="565" fill="url(#coverGlow)"/>
    <polygon points="528,212 650,188 793,188 793,174 650,174 528,198" fill="var(--silver)"/>
    <polygon points="528,446 793,410 793,430 528,466" fill="var(--red)"/>
    <polygon points="528,452 793,416 793,422 528,458" fill="var(--silver)"/>
  </svg>

  <div class="photo" role="img" aria-label="Photo: the magician on stage performing a mentalism routine with a blindfolded volunteer and a drawn portrait"
       style="left:0;top:0;width:266px;height:220px;clip-path:polygon(0 26%,45% 12%,100% 12%,100% 83%,0 100%);background:linear-gradient(160deg,#2b2f52,#12142a 60%,#3d1a1d)"></div>
  <div class="photo" role="img" aria-label="Faint illustration of a dapper figure holding a fan of playing cards"
       style="left:276px;top:0;width:242px;height:300px;background:radial-gradient(ellipse at 50% 35%,#3a3a3a,#1d1d1d 60%,rgba(30,30,30,0) 85%)"></div>
  <div class="photo" role="img" aria-label="Photo: the magician performing a rope trick with a volunteer holding scissors"
       style="left:528px;top:188px;width:265px;height:265px;clip-path:polygon(0 9%,46% 0,100% 0,100% 84%,0 98%);background:linear-gradient(150deg,#1d2450,#0e1230 55%,#3a2a2a)"></div>

  <h2 class="abs serif-heading about-heading">About Wesley</h2>
  <div class="abs body-copy about-copy">
    <p><span class="dropcap">A</span> magician as an entertainer, or speaker at your events will provide a different level of experience to your guests or clients, elevating your events!</p>
    <p>I'm a professional entertainer. I've performed all over the country for major corporations which means you're getting tried and true, first-rate entertainment. Doing business with me is easy. I make sure you're comfortable with every step in the process of dealing with me. From booking to follow-up you'll be happy. I arrive early to your event, start on time, and deliver a great performance. You might have a lot on your mind on the day of your event, but worrying about the entertainment won't be one of them.</p>
    <p>My performances are guaranteed! I pride myself on building relationships with my customers, so I'm not happy unless you're happy. I guarantee your guests will have a great time and will thank you for having me there. If you aren't thrilled with my performance, just let me know and I'll refund your money. The only reason I'm able to offer such a guarantee is because I'm very confident you will love doing business with me. In four decades of performing, I've never had anyone ask for their money back, and many of my clients hire me again and again.</p>
  </div>

  <div class="abs brand-name studio-block" style="top:294px;font-size:21px">Wesley Torvand</div>
  <div class="abs studio-block studio-name">Sleight Lane Productions</div>
  <div class="abs studio-block studio-phone">555 010 4821</div>
  <ul class="abs contact-list">
    <li><svg width="12" height="12" viewBox="0 0 12 12" aria-hidden="true"><circle cx="6" cy="6" r="5" fill="none" stroke="var(--red-bright)" stroke-width="1.3"/><path d="M1 6h10M6 1c2.4 2.8 2.4 7.2 0 10M6 1c-2.4 2.8-2.4 7.2 0 10" fill="none" stroke="var(--red-bright)" stroke-width="1"/></svg>www.wesleytorvandmagic.example</li>
    <li><svg width="12" height="10" viewBox="0 0 12 10" aria-hidden="true"><rect x=".6" y=".6" width="10.8" height="8.8" fill="none" stroke="var(--red-bright)" stroke-width="1.2"/><path d="M.6.6 6 5.5 11.4.6" fill="none" stroke="var(--red-bright)" stroke-width="1.2"/></svg>hello@wesleytorvandmagic.example</li>
    <li><svg width="12" height="12" viewBox="0 0 12 12" aria-hidden="true"><rect width="12" height="12" fill="var(--red-bright)"/></svg>/Wesley-Torvand-Magician-Mentalist</li>
  </ul>

  <div class="abs brand-name cover-title" style="top:32px;font-size:21px">Wesley Torvand</div>
  <div class="abs cover-band">CORPORATE MAGICIAN</div>
  <div class="abs cover-title cover-years">FOR OVER 40 YEARS</div>
  <div class="abs roles-pill"><span class="dot">Magician</span><span class="dot">Mentalist</span><span class="dot">Entertaner</span></div>
  <div class="abs cover-url">www.wesleytorvandmagic.example</div>
</section>

<!-- INSIDE -->
<section class="sheet sheet--inside">
  <svg class="sheet-art" width="793" height="565" viewBox="0 0 793 565" aria-hidden="true">
    <defs>
      <linearGradient id="redLeft" x1="0" y1="0" x2="0.3" y2="1">
        <stop offset="0" stop-color="#b50d14"/>
        <stop offset=".5" stop-color="#e3161e"/>
        <stop offset="1" stop-color="#8a0a0f"/>
      </linearGradient>
      <linearGradient id="redRight" x1="0" y1="0" x2="1" y2="1">
        <stop offset="0" stop-color="#8f0b10"/>
        <stop offset=".45" stop-color="#e3161e"/>
        <stop offset="1" stop-color="#a00c12"/>
      </linearGradient>
    </defs>
    <rect x="0" y="0" width="266" height="565" fill="url(#redLeft)"/>
    <rect x="266" y="0" width="262" height="565" fill="var(--black)"/>
    <rect x="528" y="0" width="265" height="565" fill="url(#redRight)"/>
    <polygon points="0,215 230,200 528,165 528,185 240,228 0,240" fill="var(--black)"/>
    <polygon points="0,222 236,206 528,172 528,178 240,214 0,228" fill="var(--silver)"/>
    <polygon points="240,228 528,185 528,192 248,236" fill="var(--red)"/>
    <polygon points="0,476 266,448 266,458 0,486" fill="var(--silver)"/>
    <polygon points="528,480 700,400 793,400 793,410 700,410 528,490" fill="var(--silver)"/>
    <polygon points="528,490 700,410 700,565 528,565" fill="var(--black)"/>
  </svg>

  <div class="photo" role="img" aria-label="Photo: the magician performing with a red silk for seated guests at a corporate banquet"
       style="left:0;top:0;width:528px;height:222px;clip-path:polygon(0 0,100% 0,100% 77%,45% 93%,0 100%);background:linear-gradient(170deg,#c9b18a 0%,#9c7d58 35%,#5a3b2c 70%,#2a1d1a)"></div>
  <div class="photo" role="img" aria-label="Photo: the magician standing beside his outdoor show stage"
       style="left:0;top:470px;width:266px;height:95px;clip-path:polygon(0 10%,100% 0,100% 100%,0 100%);background:linear-gradient(180deg,#b7bcc3,#7f8a6d 60%,#4c5340)"></div>
  <div class="photo" role="img" aria-label="Photo: a guest reacting to a close-up trick at a table"
       style="left:266px;top:455px;width:262px;height:110px;background:linear-gradient(120deg,#3d2a24,#6b4d3e 45%,#1c1616)"></div>
  <div class="photo" role="img" aria-label="Photo: portrait of the magician smiling in glasses"
       style="left:615px;top:410px;width:178px;height:155px;clip-path:polygon(48% 0,100% 0,100% 100%,0 100%,0 48%);background:linear-gradient(140deg,#4b6d8c,#c9a088 45%,#2a2c38)"></div>

  <div class="abs badge badge--dark">WHAT I DO</div>
  <ul class="abs bullets what-list">
    <li>Performed close-up</li><li>Stage shows</li>
    <li>Parlor</li><li>I've been an Master of Ceremonies</li>
  </ul>
  <p class="abs what-copy">Key Note Speaker (using magic during presentations to help build on a point ortopic, while keeping the audience entertained and educated on the topic ortopics the client has asked me to focus). I've worked trade shows andsales training incorporating magic as well. I did private shows in LasVegas and L.A. back in the late 90's as well.</p>

  <div class="abs badge badge--red">SERVICES</div>
  <p class="abs services-intro">Wesley entertains and presents key content with magic, humor and audience participation so that you learn while you laugh!</p>
  <ul class="abs bullets bullets--red services-list">
    <li>Corporate Magic</li><li>Keynote Speaker</li>
    <li>Sales Training</li><li>Magic Shows</li>
    <li>Trade Shows</li>
  </ul>

  <div class="abs promise" style="top:16px"><div class="promise-kicker">MY PERFORMANCES ARE</div><div class="promise-big">GUARANTEED!</div></div>
  <p class="abs promise-copy" style="top:67px">I pride myself on building relationships with my customers, so I'm not happy unless you're happy. I guarantee your guests will have a great time and will thank you for having me there. If you aren't thrilled with my performance, just let me know and I'll refund your money. The only reason I'm able to offer such a guarantee is because I'm very confident you will love doing business with me. In four decades of performing, I've never had anyone ask for their money back, and many of my clients hire me again and again.</p>
  <div class="abs promise" style="top:176px"><div class="promise-kicker">DOING BUSINESS WITH IS</div><div class="promise-huge">IS EASY</div></div>
  <p class="abs promise-copy" style="top:232px">I make sure you're comfortable with every step in the process of dealing with me. From booking to follow-up you'll be happy. I arrive early to your event, start on time, and deliver a great performance. You might have a lot on your mind on the day of your event, but worrying about the entertainment won't be one of them.</p>
  <div class="abs promise promise-huge" style="top:316px">I WORK CLEAN</div>
  <p class="abs promise-copy" style="top:350px">Yes, not only do I bathe every day, but all of my comedy is corporate clean. You won't hear any blue material in my show, and I won't embarrass anyone. You can rest assured that all of your guests will be treated with respect and look like stars.</p>
</section>

</body>
</html>
```